4"x9" Roofing Flyer Design - Tile Roofing!

We are looking to create a 4"x9" double sided flyer in full color that displays pictures of before and after of tile underlayment replacement. This would have words as well.

The theme should match the overall theme of our brochure that we already have designed so they are cohesive.

I have uploaded an example of a similar flyer that we like the overall layout of.

Please read the "Design Wording" PDF I uploaded for the words and overall design layout we are looking for on this brochure.

Please let me know if you'd like more photos or anything like that.

Target Market(s)

Retirees

Industry/Entity Type

Roofing

Font styles to use
Other font styles liked:
• Match existing fonts from our brochure

Requirements
Must have
• Must match style of existing brochure (uploaded), font must match closely as well

```html
<!DOCTYPE html>
<html lang="en">
<head>
<meta charset="utf-8">
<title>Granite Ridge Roofing – Tile Underlayment Flyer</title>
<link href="https://fonts.googleapis.com/css2?family=Jost:wght@400;500;700;800&family=Roboto+Condensed:wght@700&display=swap" rel="stylesheet">
<style>
  :root {
    --backdrop: #8b8a8b;
    --ink: #1b1a1b;
    --orange: #e6581d;
    --white: #ffffff;
    --photo-sky: #7f9fc4;
    --photo-tile: #4a4d55;
    --photo-tan: #b49a78;
    --photo-debris: #7d6f5e;
    --photo-felt: #8c8a80;
  }
  * { margin: 0; padding: 0; box-sizing: border-box; }
  html, body {
    width: 1200px; height: 1013px; overflow: hidden;
    background: var(--backdrop);
    font-family: "Jost", sans-serif;
  }
  .flyer-side {
    position: absolute; top: 151px;
    width: 320px; height: 720px;
    background: var(--ink);
    overflow: hidden;
    box-shadow: 0 2px 6px rgba(0,0,0,.25);
  }
  .flyer-side--front { left: 271px; }
  .flyer-side--back { left: 634px; }
  .side-shapes { position: absolute; inset: 0; width: 100%; height: 100%; }

  .copy { position: absolute; color: var(--white); }
  .copy h2, .copy h3 {
    color: var(--orange); font-weight: 800; line-height: 1.15;
  }
  .copy p { font-size: 10px; line-height: 12px; text-align: justify; }

  .front-copy { left: 16px; top: 121px; width: 272px; }
  .front-copy h2 { font-size: 10.5px; margin-bottom: 8px; }
  .front-copy h3 { font-size: 10.5px; margin: 6px 0 6px; }
  .front-copy p { margin-bottom: 6px; }

  .brand-name {
    font-family: "Jost", sans-serif; font-weight: 700;
    color: var(--ink); white-space: nowrap; text-align: center;
  }
  .brand-phone {
    font-family: "Roboto Condensed", sans-serif; font-weight: 700;
    color: var(--orange); white-space: nowrap; text-align: center;
  }
  .front-brand { position: absolute; left: 0; width: 320px; top: 612px; }
  .front-brand .brand-name { font-size: 23px; line-height: 30px; }
  .front-brand .brand-phone { font-size: 36px; line-height: 44px; margin-top: 6px; }

  .back-brand { position: absolute; left: 8px; width: 254px; top: 150px; }
  .back-brand .brand-name { font-size: 19px; line-height: 26px; }
  .back-brand .brand-phone { font-size: 30px; line-height: 36px; margin-top: 8px; }

  .back-copy { left: 21px; top: 326px; width: 280px; }
  .back-copy h2 { font-size: 11.5px; margin-bottom: 4px; text-align: justify; }
  .back-copy h3 { font-size: 11.5px; margin: 12px 0 5px; }
  .back-copy p { font-size: 11px; line-height: 13.5px; margin-bottom: 6px; }
  .back-copy .service p { text-align: left; }

  .web-address {
    position: absolute; left: 0; width: 320px; top: 657px;
    text-align: center; color: var(--white);
    font-weight: 800; font-size: 14px; line-height: 22px;
  }
  .licence {
    position: absolute; left: 0; width: 320px; top: 693px;
    text-align: center; color: var(--white);
    font-size: 11.5px; line-height: 14px;
  }
</style>
</head>
<body>

<section class="flyer-side flyer-side--front">
  <svg class="side-shapes" viewBox="0 0 557 1253" preserveAspectRatio="none" aria-hidden="false">
    <polygon fill="var(--white)" points="0,0 345,0 155,97 0,25"/>
    <polygon fill="var(--orange)" points="345,0 557,0 557,128 388,210 155,97"/>
    <polygon fill="var(--white)" points="557,128 557,290 388,210"/>
    <polygon fill="var(--white)" points="0,800 557,1050 557,1253 0,1253"/>
    <polygon role="img" aria-label="Photo: tile roof with tiles lifted for underlayment replacement" fill="var(--photo-tile)" points="30,800 262,700 262,925"/>
    <polygon role="img" aria-label="Photo: brittle, cracked old felt underlayment" fill="var(--photo-felt)" points="25,828 258,938 25,1045"/>
    <polygon role="img" aria-label="Photo: tan concrete tile roof after re-lay" fill="var(--photo-tan)" points="277,700 515,810 277,920"/>
    <polygon role="img" aria-label="Photo: crumbled underlayment debris on roof deck" fill="var(--photo-debris)" points="290,925 530,818 530,1035"/>
  </svg>

  <div class="copy front-copy">
    <h2>The Hidden Clock<br>Ticking Under Your Tiles</h2>
    <p>When a tile roof is installed, the tiles themselves are not waterproof—they are simply a shield. The actual waterproofing is done by the felt or synthetic underlayment installed beneath them.</p>
    <p>In homes of your vintage, this underlayment is now:</p>
    <h3>Brittle and Chalky</h3>
    <p>It cracks and turns into powder under the constant heat cycles, losing its waterproofing integrity.</p>
    <h3>Compromised</h3>
    <p>Even a single leak in a neighboring home means the moisture risk has increased exponentially across the entire block.</p>
    <p>Based on the age and materials used in this specific neighborhood, underlayment failure is not a matter of if, but when.</p>
    <p>Waiting for a visible ceiling stain often means the damage has already spread to the roof deck, rafters, and interior walls. A slow leak can silently cost thousands in remediation before you ever see a drop.</p>
  </div>

  <div class="front-brand">
    <div class="brand-name">Granite Ridge Roofing</div>
    <div class="brand-phone">(555) 014-2290</div>
  </div>
</section>

<section class="flyer-side flyer-side--back">
  <svg class="side-shapes" viewBox="0 0 557 1253" preserveAspectRatio="none" aria-hidden="true">
    <polygon fill="var(--orange)" points="0,0 310,0 557,120 557,475 465,435 465,245 0,12"/>
    <polygon fill="var(--white)" points="0,12 465,245 465,435 282,505 0,390"/>
    <polygon fill="var(--orange)" points="0,1142 485,1142 557,1185 75,1185"/>
  </svg>

  <div class="back-brand">
    <div class="brand-name">Granite Ridge Roofing</div>
    <div class="brand-phone">(555) 014-2290</div>
  </div>

  <div class="copy back-copy">
    <h2>Our Certified Solution: The Proactive, Full-Service Tile Lift &amp; Re-Lay</h2>
    <p>We specialize in preserving your beautiful tile roof while replacing the single most important component: the underlayment.</p>
    <p>As a licensed, bonded, and insured local contractor, we don't just replace the felt; we ensure your entire roof is built to perform:</p>
    <div class="service">
      <h3>Careful Tile Removal:</h3>
      <p>Each tile is removed by hand, inspected, and saved.</p>
      <h3>Deck Inspection:</h3>
      <p>We check for and address any underlying damage or rot.</p>
      <h3>Premium Underlayment:</h3>
      <p>We install a modern, high-grade self-adhered synthetic underlayment.</p>
      <h3>Tile Reinstallation:</h3>
      <p>Your original, attractive tiles are re-laid with new flashings and seals, ready to perform for years.</p>
    </div>
  </div>

  <div class="web-address">www.graniteridge-roofing.com</div>
  <div class="licence">AZ ROC 512077</div>
</section>

</body>
</html>
```